Desktop publishing rework of financial advisor's corporate marketing brochure

We are a financial and strategic business consultancy to corporate clients in healthcare/ pharmaceuticals. We previously had a very "wordy" slide presentation which we now thinned down to a few messages. We have created mockups of the layouts for the pages. We have also 95% finalized all wording for the pages. What we need is redesign proposals for all of the pages 1, 2, 4, 5, 6. These proposals should reflect the current layout/ arrangement of objects; they should be much more professional and generally "better looking" than what we currently have. They shall replace existing graphics with better-looking more appropriate ones.
Many thanks all

Requirements
Must have
• Use the PPT file shared below as basis

```html
<!DOCTYPE html>
<html lang="en">
<head>
<meta charset="utf-8">
<title>Larchmont Advisors – Brochure Pages</title>
<link href="https://fonts.googleapis.com/css2?family=Tinos:wght@400;700&family=Open+Sans:wght@400;600;700&display=swap" rel="stylesheet">
<style>
:root{
  --board:#a5a6a9;
  --paper:#ffffff;
  --blue:#21a9e1;
  --blue-dark:#1583b8;
  --ink:#2b2b2b;
  --charcoal:#2a2b2e;
  --grey:#7d8086;
  --grey-light:#d9dbde;
  --grey-pale:#eceef0;
}
*{box-sizing:border-box;margin:0;padding:0}
html,body{width:788px;height:1200px;overflow:hidden}
body{background:var(--board);position:relative;font-family:"Open Sans",Arial,sans-serif;color:var(--ink)}
.page{position:absolute;width:341px;height:265px;background:var(--paper);overflow:hidden;box-shadow:0 1px 4px rgba(0,0,0,.25)}
.col-l{left:50px}.col-r{left:407px}
.row-1{top:45px}.row-2{top:325px}.row-3{top:605px}.row-4{top:893px}
.abs{position:absolute}
.serif{font-family:"Tinos","Times New Roman",serif}
.brand{font-family:"Tinos","Times New Roman",serif;font-size:11px;letter-spacing:2.5px;color:var(--ink);white-space:nowrap}
.band{position:absolute;height:3px;background:var(--blue)}
.hex{position:absolute;clip-path:polygon(50% 0,100% 25%,100% 75%,50% 100%,0 75%,0 25%);display:flex;align-items:center;justify-content:center;text-align:center}
.photo{position:absolute}
.url{position:absolute;font-size:7.5px;letter-spacing:.6px;display:flex;align-items:center;gap:4px}
.url svg{width:8px;height:8px}

/* page 1 */
.cover-title{left:13px;top:58px;font-size:25px;line-height:28px;color:var(--blue)}
/* page 2 */
.stat-num{font-family:"Tinos",serif;font-size:11px;color:var(--blue);line-height:11px}
.stat-label{font-size:5px;color:var(--ink);line-height:7px}
.stat-l{right:231px;text-align:right}
.stat-r{left:232px;text-align:left}
.hero-copy{left:13px;top:40px;color:#fff;font-size:9.5px;line-height:12.5px}
/* page 3 */
.tag{left:0;top:8px;height:15px;width:186px;background:var(--blue);color:#fff;font-family:"Tinos",serif;font-size:9px;line-height:15px;padding-left:13px;clip-path:polygon(0 0,92% 0,100% 100%,0 100%)}
.logo-chip{position:absolute;height:7px;border-radius:2px;background:var(--grey-light)}
/* page 4 */
.hex-blue{background:var(--blue);color:#fff;font-size:5px;font-weight:600;line-height:7px;padding:0 8px}
.hex-white{background:#fff;color:var(--ink);font-size:5px;font-weight:600;line-height:7px;padding:0 8px}
.hex-grey{background:#9a9ca0}
/* page 5 */
.deliver-box{left:12px;top:137px;width:316px;height:71px;background:var(--blue);border-radius:4px;display:flex}
.deliver-item{flex:1;display:flex;flex-direction:column;align-items:center;justify-content:flex-end;padding-bottom:10px;color:#fff;font-size:5.5px;font-weight:600;line-height:7px;text-align:center}
.deliver-item+.deliver-item{border-left:1px solid rgba(255,255,255,.6)}
.deliver-item svg{width:22px;height:22px;margin-bottom:6px}
/* page 6 */
.work-label{font-size:5.5px;font-weight:600;color:var(--ink)}
.work-hex{position:absolute;width:32px;height:35px}
.foot-note{font-size:4.5px;font-weight:600;text-align:center;line-height:6px}
/* page 7 */
.team-side{left:0;top:0;width:96px;height:265px;background:linear-gradient(160deg,#2fb2e6,#1b8fc6 60%,#3cb8ea)}
.team-title{left:13px;top:14px;color:#fff;font-family:"Tinos",serif;font-size:9px;line-height:12px}
.portrait{position:absolute;width:38px;height:38px;border-radius:50%;border:2px solid #fff;background:radial-gradient(circle at 50% 40%,#b9bcc0,#6f7378);left:77px}
.member-name{left:122px;font-family:"Tinos",serif;font-size:5.5px;line-height:6.5px;color:var(--ink)}
.member-role{font-size:5px}
.member-bio{left:122px;width:84px;font-size:3.6px;line-height:4.6px;color:#555}
.member-points{left:213px;width:122px;font-size:3.6px;line-height:4.6px;color:#444;list-style:none}
.member-points li::before{content:"• "}
</style>
</head>
<body>

<!-- Page 1: cover -->
<section class="page col-l row-1">
  <div class="brand abs" style="right:12px;top:12px">LARCHMONT ADVISORS</div>
  <div class="photo" role="img" aria-label="Business professionals shaking hands across a meeting table" style="left:0;top:39px;width:341px;height:198px;background:linear-gradient(110deg,#3b3d40 0%,#6b6e72 45%,#a9a49a 70%,#5b5d60 100%)"></div>
  <svg class="abs" style="left:0;top:39px" width="341" height="198" viewBox="0 0 341 198">
    <polygon points="238,0 248,0 72,198 62,198" fill="#fff" opacity=".9"/>
    <polygon points="244,0 262,0 160,112 146,112" fill="var(--blue)"/>
  </svg>
  <h1 class="cover-title abs serif" style="font-weight:400">Beyond<br>Advisory</h1>
  <div class="band" style="left:200px;top:237px;width:141px"></div>
  <div class="url" style="left:15px;top:247px">
    <svg viewBox="0 0 10 10"><circle cx="5" cy="5" r="4.3" fill="none" stroke="#333" stroke-width=".9"/><ellipse cx="5" cy="5" rx="1.9" ry="4.3" fill="none" stroke="#333" stroke-width=".8"/><line x1=".7" y1="5" x2="9.3" y2="5" stroke="#333" stroke-width=".8"/></svg>
    www.larchmontadvisors.com
  </div>
</section>

<!-- Page 2: key figures -->
<section class="page col-r row-1">
  <div class="band" style="left:0;top:9px;width:140px;height:4px"></div>
  <div class="photo" role="img" aria-label="Hand holding a tablet with financial data overlays" style="left:0;top:13px;width:341px;height:92px;background:linear-gradient(90deg,#1e3552 0%,#3a5f86 45%,#8fb7d6 70%,#2a3f5a 100%)"></div>
  <p class="hero-copy abs serif">Healthcare-Focused<br>Advisor Founded by<br>Former Halvorsen Team</p>
  <div class="band" style="left:198px;top:105px;width:143px;height:4px"></div>

  <div class="abs" style="left:170px;top:120px;height:110px;border-left:1px dotted #999"></div>

  <div class="hex" style="left:117px;top:125px;width:34px;height:38px;background:var(--blue)"><svg width="16" height="12" viewBox="0 0 16 12"><circle cx="5" cy="3" r="2.2" fill="none" stroke="#fff"/><circle cx="11" cy="3" r="2.2" fill="none" stroke="#fff"/><path d="M1 11c0-3 2-4.5 4-4.5s4 1.5 4 4.5M7 11c0-3 2-4.5 4-4.5s4 1.5 4 4.5" fill="none" stroke="#fff"/></svg></div>
  <div class="hex" style="left:117px;top:159px;width:34px;height:38px;background:var(--charcoal)"><svg width="14" height="12" viewBox="0 0 14 12"><path d="M1 11h12M3 11V7M6 11V5M9 11V6M2 6l4-3 3 2 4-4" fill="none" stroke="#fff"/></svg></div>
  <div class="hex" style="left:117px;top:194px;width:34px;height:38px;background:var(--blue)"><svg width="14" height="14" viewBox="0 0 14 14"><circle cx="7" cy="5" r="3" fill="none" stroke="#fff"/><path d="M2 13c0-3 2-5 5-5s5 2 5 5" fill="none" stroke="#fff"/></svg></div>
  <div class="hex" style="left:189px;top:125px;width:34px;height:38px;background:var(--charcoal)"><svg width="14" height="13" viewBox="0 0 14 13"><rect x="1" y="2" width="12" height="10" fill="none" stroke="#fff"/><path d="M1 5h12M4 0v3M10 0v3" stroke="#fff"/></svg></div>
  <div class="hex" style="left:189px;top:159px;width:34px;height:38px;background:var(--blue)"><svg width="14" height="13" viewBox="0 0 14 13"><rect x="1" y="1" width="12" height="9" fill="none" stroke="#fff"/><path d="M3 8l3-3 2 2 3-3M5 12h4" fill="none" stroke="#fff"/></svg></div>
  <div class="hex" style="left:189px;top:194px;width:34px;height:38px;background:var(--charcoal)"><svg width="13" height="13" viewBox="0 0 13 13"><circle cx="5.5" cy="5.5" r="4" fill="none" stroke="#fff" stroke-width="1.2"/><path d="M8.5 8.5l3.5 3.5" stroke="#fff" stroke-width="1.4"/></svg></div>

  <div class="abs stat-l" style="top:137px"><div class="stat-num">15</div><div class="stat-label">Senior Professionals</div></div>
  <div class="abs stat-l" style="top:171px"><div class="stat-num">&gt;$150bn</div><div class="stat-label">Transacted Deal Value</div></div>
  <div class="abs stat-l" style="top:206px"><div class="stat-num">15</div><div class="stat-label">CEO Posts Held</div></div>
  <div class="abs stat-r" style="top:137px"><div class="stat-num">25yrs</div><div class="stat-label">Average Experience</div></div>
  <div class="abs stat-r" style="top:171px"><div class="stat-num">&gt;100</div><div class="stat-label">Individual Transactions</div></div>
  <div class="abs stat-r" style="top:206px"><div class="stat-num">&gt;20</div><div class="stat-label">C-Suite Positions Held</div></div>

  <div class="band" style="left:0;top:260px;width:341px;height:4px"></div>
</section>

<!-- Page 3: expertise -->
<section class="page col-l row-2">
  <div class="tag abs">Deep Complementary Senior Expertise</div>
  <div class="abs" style="left:0;top:0;width:341px;height:265px">
    <div class="logo-chip" style="left:6px;top:37px;width:50px"></div><div class="logo-chip" style="left:80px;top:33px;width:18px;height:12px"></div><div class="logo-chip" style="left:122px;top:37px;width:40px"></div><div class="logo-chip" style="left:180px;top:37px;width:38px"></div><div class="logo-chip" style="left:236px;top:37px;width:36px"></div><div class="logo-chip" style="left:296px;top:37px;width:38px"></div>
    <div class="logo-chip" style="left:6px;top:58px;width:46px"></div><div class="logo-chip" style="left:72px;top:56px;width:32px;height:10px"></div><div class="logo-chip" style="left:116px;top:56px;width:38px;height:10px"></div><div class="logo-chip" style="left:168px;top:56px;width:44px;height:12px"></div><div class="logo-chip" style="left:236px;top:57px;width:28px"></div><div class="logo-chip" style="left:276px;top:54px;width:18px;height:14px;border-radius:50%"></div><div class="logo-chip" style="left:304px;top:57px;width:30px"></div>
    <div class="logo-chip" style="left:22px;top:78px;width:14px;height:10px"></div><div class="logo-chip" style="left:90px;top:78px;width:22px;height:10px"></div><div class="logo-chip" style="left:125px;top:77px;width:18px;height:12px"></div><div class="logo-chip" style="left:157px;top:79px;width:42px"></div><div class="logo-chip" style="left:212px;top:77px;width:38px;height:10px"></div><div class="logo-chip" style="left:258px;top:79px;width:26px"></div><div class="logo-chip" style="left:292px;top:79px;width:42px"></div>
    <div class="logo-chip" style="left:6px;top:98px;width:44px"></div><div class="logo-chip" style="left:60px;top:98px;width:36px"></div><div class="logo-chip" style="left:288px;top:98px;width:42px"></div><div class="logo-chip" style="left:262px;top:96px;width:12px;height:10px"></div>
    <div class="logo-chip" style="left:6px;top:118px;width:40px"></div><div class="logo-chip" style="left:64px;top:118px;width:40px"></div><div class="logo-chip" style="left:262px;top:118px;width:30px"></div><div class="logo-chip" style="left:300px;top:116px;width:30px;height:10px"></div>
    <div class="logo-chip" style="left:12px;top:138px;width:14px;height:12px"></div><div class="logo-chip" style="left:42px;top:140px;width:30px"></div><div class="logo-chip" style="left:82px;top:140px;width:40px"></div><div class="logo-chip" style="left:238px;top:141px;width:52px"></div><div class="logo-chip" style="left:302px;top:139px;width:30px"></div>
    <div class="logo-chip" style="left:6px;top:160px;width:36px"></div><div class="logo-chip" style="left:62px;top:158px;width:20px;height:10px"></div><div class="logo-chip" style="left:122px;top:160px;width:46px"></div><div class="logo-chip" style="left:180px;top:160px;width:42px"></div><div class="logo-chip" style="left:246px;top:158px;width:42px;height:10px"></div><div class="logo-chip" style="left:302px;top:158px;width:32px;height:12px"></div>
    <div class="logo-chip" style="left:8px;top:180px;width:36px"></div><div class="logo-chip" style="left:62px;top:182px;width:36px"></div><div class="logo-chip" style="left:160px;top:178px;width:60px"></div><div class="logo-chip" style="left:250px;top:182px;width:44px"></div><div class="logo-chip" style="left:302px;top:180px;width:32px"></div>
    <div class="logo-chip" style="left:28px;top:198px;width:14px;height:14px"></div><div class="logo-chip" style="left:58px;top:202px;width:42px"></div><div class="logo-chip" style="left:142px;top:202px;width:26px"></div><div class="logo-chip" style="left:210px;top:200px;width:26px;height:12px;border-radius:50%"></div><div class="logo-chip" style="left:298px;top:202px;width:36px"></div>
    <div class="logo-chip" style="left:10px;top:222px;width:40px"></div><div class="logo-chip" style="left:72px;top:220px;width:28px;height:10px"></div><div class="logo-chip" style="left:120px;top:222px;width:40px"></div><div class="logo-chip" style="left:176px;top:220px;width:22px;height:12px"></div><div class="logo-chip" style="left:218px;top:222px;width:30px"></div><div class="logo-chip" style="left:260px;top:222px;width:36px"></div>
  </div>
  <div class="brand abs" style="left:103px;top:120px;font-size:13px;letter-spacing:2px;background:#fff;padding:2px 4px">LARCHMONT ADVISORS</div>
  <svg class="abs" style="left:0;top:0" width="341" height="265" viewBox="0 0 341 265">
    <defs><marker id="tip" viewBox="0 0 6 6" refX="4" refY="3" markerWidth="5" markerHeight="5" orient="auto"><path d="M0 0L6 3 0 6z" fill="var(--blue)"/></marker></defs>
    <path d="M78 82c-8 14 0 26 20 26" fill="none" stroke="var(--blue)" stroke-width="2.5" marker-end="url(#tip)"/>
    <path d="M285 82c-10-8-24-4-28 10" fill="none" stroke="var(--blue)" stroke-width="2.5" marker-end="url(#tip)"/>
    <path d="M160 188c14 2 22-8 24-18" fill="none" stroke="var(--blue)" stroke-width="2.5" marker-end="url(#tip)"/>
  </svg>
  <div class="band" style="left:0;top:260px;width:341px;height:4px"></div>
</section>

<!-- Page 4: approach -->
<section class="page col-r row-2">
  <div class="brand abs" style="left:12px;top:14px">LARCHMONT ADVISORS</div>
  <div class="photo" role="img" aria-label="Upward view of dark glass office towers" style="left:0;top:38px;width:341px;height:188px;background:linear-gradient(180deg,#3a3b3e,#202124 60%,#2c2d30)"></div>
  <div class="hex hex-blue" style="left:11px;top:80px;width:64px;height:72px">UNIQUE APPROACH TO DELIVERING CLIENT SUCCESS</div>
  <div class="hex hex-blue" style="left:113px;top:80px;width:64px;height:72px">TRANSACTION STRATEGY MANAGEMENT</div>
  <div class="hex hex-blue" style="left:214px;top:80px;width:64px;height:72px">ENABLE AND PURSUE</div>
  <div class="hex hex-white" style="left:63px;top:140px;width:64px;height:72px;padding-top:6px">SEAMLESS INTEGRATION OF DISCIPLINES</div>
  <div class="hex hex-white" style="left:165px;top:140px;width:64px;height:72px;padding-top:6px">CONSOLIDATED OUTPUT</div>
  <div class="hex hex-white" style="left:265px;top:140px;width:64px;height:72px;padding-top:6px">SUCCESSFUL TRANSACTIONS &amp; CORPORATE EVOLUTIONS</div>
  <div class="hex hex-grey" style="left:83px;top:120px;width:24px;height:27px"><svg width="12" height="10" viewBox="0 0 12 10"><path d="M1 1h8v5H4L2 8V6H1z" fill="none" stroke="#fff"/></svg></div>
  <div class="hex hex-grey" style="left:184px;top:120px;width:24px;height:27px"><svg width="12" height="10" viewBox="0 0 12 10"><rect x="1" y="1" width="10" height="6" fill="none" stroke="#fff"/><circle cx="6" cy="4" r="1.5" fill="#fff"/></svg></div>
  <div class="hex hex-grey" style="left:285px;top:120px;width:24px;height:27px"><svg width="12" height="12" viewBox="0 0 12 12"><circle cx="6" cy="6" r="3" fill="none" stroke="#fff" stroke-width="1.6" stroke-dasharray="2 1"/><circle cx="6" cy="6" r="1" fill="#fff"/></svg></div>
  <div class="hex hex-grey" style="left:134px;top:145px;width:24px;height:27px"><svg width="13" height="9" viewBox="0 0 13 9"><circle cx="3" cy="3" r="1.6" fill="#fff"/><circle cx="6.5" cy="2.5" r="1.8" fill="#fff"/><circle cx="10" cy="3" r="1.6" fill="#fff"/><path d="M0 9c0-3 6-3 6.5-3s6.5 0 6.5 3z" fill="#fff"/></svg></div>
  <div class="hex hex-grey" style="left:234px;top:145px;width:24px;height:27px"><svg width="9" height="12" viewBox="0 0 9 12"><rect x=".5" y="1" width="8" height="10.5" fill="none" stroke="#fff"/><path d="M2 4h5M2 6h5M2 8h5" stroke="#fff" stroke-width=".8"/></svg></div>
  <div class="band" style="left:198px;top:226px;width:143px;height:4px"></div>
  <div class="band" style="left:0;top:260px;width:341px;height:4px"></div>
</section>

<!-- Page 5: delivery office -->
<section class="page col-l row-3">
  <div class="band" style="left:250px;top:30px;width:91px;height:10px;clip-path:polygon(8% 0,100% 0,100% 100%,0 100%)"></div>
  <div class="photo" role="img" aria-label="Business people reviewing charts at a desk, dark toned" style="left:0;top:40px;width:341px;height:117px;background:linear-gradient(90deg,#3c3d40,#5a5c60 50%,#3a3b3e)"></div>
  <p class="abs serif" style="left:0;width:341px;top:88px;text-align:center;color:#fff;font-size:9px;line-height:12.5px">OUTSOURCED SOLUTION DELIVERY OFFICE<br>for Our Clients – Enhanced Insight</p>
  <div class="deliver-box abs">
    <div class="deliver-item"><svg viewBox="0 0 22 22"><path d="M9 2l4 2-5 9-3-2zM4 20h14M6 20c0-4 3-6 7-6M13 14a3 3 0 0 0 3-5" fill="none" stroke="#222" stroke-width="1.6"/></svg>UNDERSTAND<br>SITUATIONS</div>
    <div class="deliver-item"><svg viewBox="0 0 22 22"><circle cx="6" cy="14" r="4.5" fill="none" stroke="#222" stroke-width="1.6"/><circle cx="16" cy="14" r="4.5" fill="none" stroke="#222" stroke-width="1.6"/><path d="M8 9l1-4h4l1 4M10.5 14h1" stroke="#222" stroke-width="1.6" fill="none"/></svg>IDENTIFY<br>DIRECTIONS</div>
    <div class="deliver-item"><svg viewBox="0 0 22 22"><rect x="3" y="3" width="13" height="17" fill="none" stroke="#222" stroke-width="1.6"/><path d="M6 8h7M6 11h7M6 14h5M20 3l-8 11" stroke="#222" stroke-width="1.6"/></svg>INFORM<br>DECISION-MAKING</div>
  </div>
  <p class="abs serif" style="left:0;width:341px;top:224px;text-align:center;font-size:8.5px">Baseline: Flawless Successful Execution Throughout</p>
  <div class="band" style="left:0;top:260px;width:341px;height:4px"></div>
</section>

<!-- Page 6: areas of work -->
<section class="page col-r row-3">
  <p class="abs serif" style="left:0;width:341px;top:20px;text-align:center;font-size:8.5px;line-height:12px">OUTSOURCED SOLUTION DELIVERY OFFICE<br><span style="color:var(--blue)">Areas of Work</span></p>
  <svg class="abs" style="left:0;top:0" width="341" height="265" viewBox="0 0 341 265">
    <circle cx="161" cy="139" r="74" fill="none" stroke="#7fcbee" stroke-width=".8" stroke-dasharray="1.5 2"/>
    <g fill="var(--blue)"><circle cx="117" cy="80" r="2"/><circle cx="105" cy="116" r="2"/><circle cx="105" cy="161" r="2"/><circle cx="117" cy="198" r="2"/><circle cx="207" cy="80" r="2"/><circle cx="218" cy="116" r="2"/><circle cx="218" cy="161" r="2"/><circle cx="207" cy="198" r="2"/></g>
    <g fill="#fff" stroke="var(--blue)" stroke-width="3">
      <polygon points="85,61 99,69 99,85 85,93 71,85 71,69"/>
      <polygon points="65,100 79,108 79,124 65,132 51,124 51,108"/>
      <polygon points="65,147 79,155 79,171 65,179 51,171 51,155"/>
      <polygon points="85,187 99,195 99,211 85,219 71,211 71,195"/>
      <polygon points="239,61 253,69 253,85 239,93 225,85 225,69"/>
      <polygon points="259,100 273,108 273,124 259,132 245,124 245,108"/>
      <polygon points="259,147 273,155 273,171 259,179 245,171 245,155"/>
      <polygon points="239,187 253,195 253,211 239,219 225,211 225,195"/>
      <polygon points="161,104 193,121 193,157 161,174 129,157 129,121" stroke-width="6"/>
    </g>
    <g fill="none" stroke="#222" stroke-width="1.4">
      <circle cx="84" cy="76" r="4"/><path d="M87 79l4 4"/>
      <rect x="59" y="112" width="12" height="8"/><path d="M57 122h16"/>
      <path d="M59 158h11v7h-7l-3 3v-3h-1z"/>
      <circle cx="85" cy="203" r="6"/><path d="M85 199v8"/>
      <circle cx="239" cy="74" r="3"/><path d="M233 84c0-4 3-6 6-6s6 2 6 6z"/>
      <circle cx="259" cy="116" r="5"/><path d="M259 111l3-2M259 121l-3 2"/>
      <circle cx="259" cy="163" r="5"/><circle cx="259" cy="163" r="2"/>
      <circle cx="239" cy="201" r="3.5"/><path d="M239 194v-2M246 201h2M230 201h2M237 206h4"/>
    </g>
  </svg>
  <div class="photo" role="img" aria-label="Puzzle-piece head illustration in blue and grey" style="left:141px;top:121px;width:40px;height:36px;border-radius:3px;background:linear-gradient(90deg,#a6a9ad 50%,#1f3d6e 50%)"></div>
  <p class="abs" style="left:136px;top:82px;width:50px;text-align:center;font-size:3.2px;line-height:3.8px;font-weight:700">STRATEGIZE<br>ADJUST<br>IMPLEMENT<br>MONITOR</p>
  <p class="abs" style="left:116px;top:180px;width:90px;text-align:center;font-size:3.2px;line-height:3.8px;font-weight:700">SENIOR MANAGEMENT:<br>Companies - Businesses - Portfolios - Products</p>
  <span class="abs work-label" style="left:35px;top:72px">IDENTIFY</span>
  <span class="abs work-label" style="left:18px;top:112px">SCREEN</span>
  <span class="abs work-label" style="left:20px;top:160px">REVIEW</span>
  <span class="abs work-label" style="left:33px;top:200px">TRANSACT</span>
  <span class="abs work-label" style="left:265px;top:72px">EXECUTE</span>
  <span class="abs work-label" style="left:282px;top:112px">APPROACH</span>
  <span class="abs work-label" style="left:282px;top:160px">PREPARE</span>
  <span class="abs work-label" style="left:261px;top:200px">PLAN</span>
  <p class="abs foot-note" style="left:20px;top:230px;width:120px">INWARD TRANSACTIONS:<br>Buy - In-License - Partner - Invest</p>
  <p class="abs foot-note" style="left:200px;top:230px;width:130px">OUTWARD TRANSACTIONS:<br>Sell - Out-License - Partner - Re-Finance</p>
  <div class="band" style="left:0;top:260px;width:341px;height:4px"></div>
</section>

<!-- Page 7: key team -->
<section class="page col-l row-4">
  <div class="team-side abs" role="img" aria-label="Blue-tinted glass building facade"></div>
  <p class="team-title abs">KEY TEAM<br>Members</p>

  <div class="portrait" style="top:21px" role="img" aria-label="Portrait of Omar Ellison"></div>
  <div class="member-name abs" style="top:23px">OMAR ELLISON, MBBS<br><span class="member-role">Founder &amp; Strategic Lead</span></div>
  <p class="member-bio abs" style="top:38px">Senior biotech strategy advisor and negotiator with multidisciplinary strategic mindset.</p>
  <ul class="member-points abs" style="top:23px"><li>Led Halvorsen's health care advisory globally</li><li>Prior roles at Carrow Brothers and Nordbank</li><li>Successful track record across market cycles</li><li>Hands-on clinical experience</li><li>Trained surgeon, BSc, MBBS, MRCS, MBA</li></ul>

  <div class="portrait" style="top:67px" role="img" aria-label="Portrait of Felix Hartung"></div>
  <div class="member-name abs" style="top:70px">FELIX HARTUNG, MHMM<br><span class="member-role">Founder &amp; Execution Lead</span></div>
  <p class="member-bio abs" style="top:85px">Senior biotech transaction advisor with track record of successful execution in "usual" and "turn-around" situations.</p>
  <ul class="member-points abs" style="top:70px"><li>Buy-side &amp; sell-side transaction origination and execution as well as financings (Halvorsen, Nordbank)</li><li>Deep coverage across healthcare segments</li><li>Financial and operational restructuring &amp; turn-around</li><li>Trained in business and medicinal science</li></ul>

  <div class="portrait" style="top:114px" role="img" aria-label="Portrait of Conor Whitfield"></div>
  <div class="member-name abs" style="top:116px">CONOR WHITFIELD<br><span class="member-role">Head of Biopharma</span></div>
  <p class="member-bio abs" style="top:131px">Successful serial CEO and board member with track record of successful financing, repositioning and exiting.</p>
  <ul class="member-points abs" style="top:116px"><li>Includes a $600m sale to Veltra Pharma</li><li>Formerly Corporate &amp; Business Development leader (Aurel, Kestrel Health) and roles across the value chain at Orvane, Meridian Labs, Halden</li><li>Pharmacologist by training</li></ul>

  <div class="portrait" style="top:161px" role="img" aria-label="Portrait of Paul Redgrave"></div>
  <div class="member-name abs" style="top:163px">PAUL REDGRAVE, PHD<br><span class="member-role">Portfolio and Strategy</span></div>
  <p class="member-bio abs" style="top:178px">Successful corporate development strategist with track record in internal &amp; external business building.</p>
  <ul class="member-points abs" style="top:163px"><li>Led the development and implementation of various success strategies across the value chain</li><li>Former Head of Corporate Development (Lumeris)</li><li>Strategy consultant (Brantley Group)</li><li>Biochemist by training including at Eastbridge Cancer Institute</li></ul>

  <div class="portrait" style="top:207px" role="img" aria-label="Portrait of Simon Ashby"></div>
  <div class="member-name abs" style="top:209px">SIMON ASHBY, PHD<br><span class="member-role">Industry Relations</span></div>
  <p class="member-bio abs" style="top:224px">Senior corporate development leader with string of success in transaction origination and execution.</p>
  <ul class="member-points abs" style="top:209px"><li>Led creation of Cancer Research Trust's screening &amp; evaluation committee deploying GBP500m p.a.</li><li>Corp. &amp; Bus. Dev. leader (Corvana) orchestrating review of countless assets</li><li>Biotech C-suite member</li><li>Product development positions</li><li>Pharmacologist by training</li></ul>

  <p class="abs" style="left:100px;top:252px;font-size:4.5px;font-weight:600">Diverse Senior Team with Deep Combined Domain and Transaction Expertise.</p>
</section>

<!-- Page 8: global coverage -->
<section class="page col-r row-4">
  <div class="brand abs" style="left:15px;top:33px">LARCHMONT ADVISORS</div>
  <div class="band" style="left:198px;top:53px;width:143px;height:6px"></div>
  <div class="photo" role="img" aria-label="Grey world map with blue location pins over dark city skyline" style="left:0;top:59px;width:341px;height:170px;background:radial-gradient(ellipse at 40% 45%,#6d6f73,#2c2d30 70%)"></div>
  <p class="abs serif" style="left:224px;top:131px;color:var(--blue);font-size:9.5px">GLOBAL COVERAGE</p>
  <p class="abs serif" style="left:224px;top:145px;color:#fff;font-size:7px">Revenue Split: 85%, 10%, 5%</p>
  <div class="band" style="left:0;top:229px;width:143px;height:4px"></div>
  <div class="url" style="left:13px;top:244px">
    <svg viewBox="0 0 10 10"><circle cx="5" cy="5" r="4.3" fill="none" stroke="#333" stroke-width=".9"/><ellipse cx="5" cy="5" rx="1.9" ry="4.3" fill="none" stroke="#333" stroke-width=".8"/><line x1=".7" y1="5" x2="9.3" y2="5" stroke="#333" stroke-width=".8"/></svg>
    www.larchmontadvisors.com
  </div>
</section>

</body>
</html>
```